Single Page Production Company Site

Clean. Simple. Minimalist site with one page.

No portfolio, just some text to communicate a general overview of what the company does.

We work for a very select group of clients, creating strong brand personalities online. The site is specifically minimal and not communicating too much about what we do.. we have a variety of capabilities to work with clients and prefer to be broad with just a simple landing page as the point of contact for our brand.
Updates

Christmas holidays are coming up, maybe people need some time away from work with family and friends... We can keep working on this and I will provide feedback as quickly as possible, but I understand if designers have other commitments during the coming days. Thanks for your hard work!

Industry/Entity Type

Design Agency

Coding

Coded - Design and coding required

Number of Pages Required

1 page

Font styles to use
Sans Serif

Requirements
Must have
• Clean, bold text headlines.
Nice to have
• Unsure about any images used in the design, would like to see options with or without.

```html
<!DOCTYPE html>
<html lang="en">
<head>
<meta charset="utf-8">
<title>Cedar Development Co</title>
<link href="https://fonts.googleapis.com/css2?family=Bebas+Neue&family=Montserrat:wght@400;500;600&display=swap" rel="stylesheet">
<style>
:root{
  --brown:#4a342e;
  --brown-dark:#3d2a25;
  --footer:#3f2c27;
  --ink:#2d2d2d;
  --text:#4a4a4a;
  --muted:#6d6d6d;
  --soft:#f2f2f2;
  --white:#ffffff;
}
*{margin:0;padding:0;box-sizing:border-box}
html,body{width:1200px;height:4833px;overflow:hidden}
body{position:relative;background:var(--white);font-family:"Montserrat",sans-serif;color:var(--text)}
.abs{position:absolute}
.headline{font-family:"Bebas Neue",sans-serif;font-weight:400;color:var(--ink);letter-spacing:.5px}
.rule{display:block;width:70px;height:3px;background:var(--brown);margin:0 auto}

/* hero */
.hero{left:0;top:0;width:1200px;height:672px;overflow:hidden}
.hero-photo{position:absolute;inset:0;background:linear-gradient(180deg,#3c3a47 0%,#b4563a 18%,#d9793d 30%,#6f4a3c 48%,#3b4a34 68%,#2b3524 100%)}
.hero-wave{position:absolute;left:0;top:0}
.brand{left:110px;top:26px;font-family:"Bebas Neue",sans-serif;font-size:38px;color:var(--white);letter-spacing:1px}
.nav{right:112px;top:36px;display:flex;gap:24px;list-style:none}
.nav li{font-size:15px;color:var(--white);letter-spacing:.3px}
.hero-title{left:0;width:1200px;top:198px;text-align:center;font-family:"Bebas Neue",sans-serif;font-size:58px;color:var(--white);letter-spacing:1px}
.hero-rule{left:565px;top:284px;width:70px;height:2px;background:var(--white)}
.hero-sub{left:290px;width:620px;top:322px;text-align:center;font-size:15px;line-height:24px;color:var(--white)}

/* features */
.feature{width:300px;text-align:center}
.feature-icon{width:114px;height:114px;border-radius:50%;background:var(--brown);margin:0 auto 28px;display:flex;align-items:center;justify-content:center}
.feature-icon.raised{box-shadow:0 8px 18px rgba(0,0,0,.35)}
.feature h3{font-size:20px;font-weight:500;color:var(--ink);margin-bottom:16px}
.feature p{font-size:13px;line-height:20.5px;color:var(--muted);padding:0 18px}

/* about */
.about-bg{left:0;top:1040px}
.about{left:112px;width:976px;top:1216px;text-align:center}
.about h2{font-size:40px;margin-bottom:14px}
.about p{font-size:14.5px;line-height:24px;color:var(--text);margin-top:24px}
.about p:first-of-type{margin-top:44px}
.btn{display:inline-block;background:var(--brown-dark);color:var(--white);font-size:15px;padding:13px 16px;border-radius:2px}
.about .btn{margin-top:40px}

/* stories */
.blob{left:0;top:0}
.story{width:432px}
.story h2{font-size:30px;margin-bottom:20px}
.story p{font-size:13.5px;line-height:20.5px;text-align:justify;margin-bottom:18px;color:var(--ink)}
.story .lead{font-size:15.5px;line-height:22px;font-weight:500;text-align:left}
.art{border-radius:14px}

/* contact */
.contact-title{left:0;width:1200px;top:4020px;text-align:center}
.contact-title h2{font-size:40px;margin-bottom:12px}
.field{background:var(--white);box-shadow:0 3px 10px rgba(0,0,0,.12);font-size:13px;color:var(--muted);padding:19px 26px}

/* footer */
.footer{left:0;top:4596px;width:1200px;height:237px;background:var(--footer)}
.footer-brand{left:110px;top:86px;font-family:"Bebas Neue",sans-serif;font-size:38px;color:var(--white);letter-spacing:1px}
.mail{right:112px;top:66px;display:flex;align-items:center;gap:16px;color:var(--white);font-size:17px}
.mail-icon{width:40px;height:40px;border-radius:50%;background:var(--white);display:flex;align-items:center;justify-content:center}
.footer-rule{left:600px;top:126px;width:488px;height:1px;background:rgba(255,255,255,.5)}
.copyright{right:112px;top:176px;color:var(--white);font-size:14px}
</style>
</head>
<body>

<header class="abs hero">
  <div class="hero-photo" role="img" aria-label="Photo of a wooden path along a green ridge under an orange sunset sky"></div>
  <svg class="hero-wave" width="1200" height="672" viewBox="0 0 1200 672">
    <path d="M0 672 C 220 650 470 520 700 530 C 880 540 980 600 1200 545 L1200 672 Z" fill="#ffffff"/>
  </svg>
  <div class="abs brand">Cedar Development Co</div>
  <ul class="abs nav">
    <li>HOME</li><li>COMPANY</li><li>SERVICES</li><li>OUR WORK</li><li>BLOG</li><li>CONTACT US</li>
  </ul>
  <h1 class="abs hero-title">CONCEPT. CREATE. COMPLETE.</h1>
  <span class="abs hero-rule"></span>
  <p class="abs hero-sub">At Cedar Development Company, we are leading the way in design innovation for modern websites.</p>
</header>

<section>
  <div class="abs feature" style="left:96px;top:736px">
    <div class="feature-icon">
      <svg width="46" height="46" viewBox="0 0 46 46" fill="none" stroke="#fff" stroke-width="2.2" stroke-linecap="round">
        <rect x="19" y="4" width="8" height="22" rx="1"/><path d="M19 26 L23 34 L27 26"/><path d="M8 40 L38 40"/><path d="M12 40 L8 30 M34 40 L38 30"/><circle cx="8" cy="29" r="2"/><circle cx="38" cy="29" r="2"/>
      </svg>
    </div>
    <h3>Design Happens Here</h3>
    <p>We are leading the way in design innovation for modern websites. Clean, functional, intuitive websites for progressive businesses.</p>
  </div>
  <div class="abs feature" style="left:450px;top:736px">
    <div class="feature-icon raised">
      <svg width="46" height="46" viewBox="0 0 46 46" fill="none" stroke="#fff" stroke-width="2.2" stroke-linecap="round" stroke-linejoin="round">
        <rect x="6" y="12" width="26" height="26"/><path d="M16 30 L18 24 L38 6 L42 10 L24 28 Z"/><path d="M6 42 L36 42"/>
      </svg>
    </div>
    <h3>Art Happens Here</h3>
    <p>Building brands through design, we believe that contrast is everything. For industry leaders who set the pace and exceed expectations, we help give the company voice and soul.</p>
  </div>
  <div class="abs feature" style="left:803px;top:736px">
    <div class="feature-icon">
      <svg width="46" height="46" viewBox="0 0 46 46" fill="none" stroke="#fff" stroke-width="2.2" stroke-linecap="round">
        <path d="M15 22 A8 8 0 1 1 31 22 C31 27 27 28 27 33 L19 33 C19 28 15 27 15 22 Z"/><path d="M19 37 L27 37 M20 41 L26 41"/><path d="M23 4 L23 7 M9 10 L11 12 M37 10 L35 12 M5 22 L8 22 M41 22 L38 22"/>
      </svg>
    </div>
    <h3>Idea Happens Here</h3>
    <p>Clients look to us for unique, exceptional solutions to their technology issues. We bring creativity to the table and solve your business’ problems with actionable solutions.</p>
  </div>
</section>

<section>
  <svg class="abs about-bg" width="1200" height="604" viewBox="0 0 1200 604">
    <path d="M0 18 C 300 110 700 110 1200 30 L1200 604 L0 604 Z" fill="#f2f2f2"/>
  </svg>
  <div class="abs about">
    <h2 class="headline">ABOUT CEDAR DEVELOPMENT</h2>
    <span class="rule"></span>
    <p>Having a website isn't enough. You need to show your customers you understand the internet. Our design professionals will give your site an up-to-date look without overwhelming your customers with bells and whistles. Your website will be fast.</p>
    <p>Intuitive, and informative - customers will find what they need quickly and be satisfied with the experience. Our team can update your website with the most up-to-date enhancements.</p>
    <span class="btn">Read More</span>
  </div>
</section>

<svg class="abs blob" width="1200" height="4833" viewBox="0 0 1200 4833" aria-hidden="true">
  <path d="M1200 1725 C 1100 1720 1000 1760 900 1830 C 800 1890 700 1840 610 1930 C 540 2010 560 2150 680 2200 C 820 2250 1000 2200 1200 2215 Z" fill="#f2f2f2"/>
  <path d="M0 2250 C 150 2240 260 2390 420 2380 C 560 2375 640 2450 620 2560 C 600 2680 480 2770 300 2740 C 180 2720 90 2760 0 2760 Z" fill="#f2f2f2"/>
  <path d="M1200 2728 C 1080 2730 980 2840 820 2830 C 680 2820 600 2900 600 3010 C 600 3150 720 3290 900 3270 C 1040 3255 1120 3240 1200 3290 Z" fill="#f2f2f2"/>
  <path d="M0 3225 C 120 3240 240 3330 420 3330 C 560 3330 640 3420 615 3530 C 590 3650 460 3720 300 3700 C 180 3685 80 3720 0 3730 Z" fill="#f2f2f2"/>
  <path d="M0 3850 C 300 3895 800 3900 1200 3855 L1200 3870 C 800 3920 300 3915 0 3870 Z" fill="#f6f6f6"/>
</svg>

<section>
  <div class="abs story" style="left:112px;top:1892px">
    <h2 class="headline">SIZE IS EVERYTHING.</h2>
    <p>We don’t work in a massive corporate office and we don’t have a mailroom. Not that there’s anything wrong with that, it’s just that we like knowing each other’s names, and encourage our clients to know ours.</p>
    <p>Our small staff has an advantage – our group works more efficiently, more cost-effectively and most importantly, flexible to each client’s unique needs. We deliver a range of services found at any agency, with the personal service you should expect.</p>
  </div>
  <div class="abs art" style="left:648px;top:1903px;width:450px;height:264px;background:linear-gradient(135deg,#cfdbe4,#2c3e58 60%,#f2b24a)" role="img" aria-label="Illustration of a small team working together at desks with computer screens"></div>

  <div class="abs art" style="left:112px;top:2437px;width:372px;height:272px;background:linear-gradient(135deg,#e8eef3,#b8c8d6 45%,#1f2b4a 75%,#e56b8a)" role="img" aria-label="Illustration of two people planning in front of a large dashboard with plants beside them"></div>
  <div class="abs story" style="left:658px;top:2421px">
    <h2 class="headline">OUR GOAL.</h2>
    <p>Cedar Development brings your brand to life, online. We do it all when it comes to online commerce for retail stores, wholesalers and distributors.</p>
    <p>Taking your company online introduces a world of opportunity, as well as specific challenges associated with online trade. We’ll assist you in establishing a successful online presence and bringing your brand to a worldwide audience.</p>
  </div>

  <div class="abs story" style="left:112px;top:2891px">
    <h2 class="headline">WHO'S REID?</h2>
    <p>Reid Halloway, owner of Cedar Development is not your typical principal. He’s worked internationally with both Larkmoor and Brightwell Media publications in photo production for titles including Metropolis Weekly and Gilded Mirror.</p>
    <p>Originally from coastal Maine and an all-around New Englander, Reid can often be found sailing during the summer and skiing during winter. He believes that inspiration comes from experiencing the world, not from sitting in a cubicle. But no worries, his biggest fear is being offline, and is always within an arms reach of the Internet.</p>
  </div>
  <div class="abs art" style="left:760px;top:2897px;width:318px;height:290px;background:linear-gradient(135deg,#dfe6ef,#8fb6f0 45%,#2b2b4a 70%,#b46a3a)" role="img" aria-label="Illustration of a man working on a laptop in front of code screens and plants"></div>

  <div class="abs art" style="left:109px;top:3409px;width:326px;height:247px;background:linear-gradient(135deg,#1d1d1d,#3ba7d6 45%,#8cc63f 65%,#f26a2e)" role="img" aria-label="Illustration of a laptop with a magnifying glass over gears"></div>
  <div class="abs story" style="left:658px;top:3382px">
    <h2 class="headline">WE GET YOU.</h2>
    <p>Having a website isn't enough. You need to show your customers you understand the socially connected online world we live in. We help you create designs that capture the personality of your business and project the image you want your customers to see.</p>
    <p>Maybe you’re a small company looking to sell yourself in the big leagues; maybe you’re a big company that wants to look approachable; either way, we can make it happen.</p>
    <p class="lead">You’ll come across looking professional, unique and strikingly hip all at the same time.</p>
  </div>
</section>

<section>
  <div class="abs contact-title">
    <h2 class="headline">CONTACT FORM</h2>
    <span class="rule"></span>
  </div>
  <div class="abs field" style="left:189px;top:4146px;width:822px;height:48px">Full Name</div>
  <div class="abs field" style="left:189px;top:4207px;width:402px;height:51px">Phone Number</div>
  <div class="abs field" style="left:606px;top:4207px;width:405px;height:51px">Email Address</div>
  <div class="abs field" style="left:189px;top:4271px;width:822px;height:161px">Message</div>
  <span class="abs btn" style="left:534px;top:4464px;width:132px;height:43px;text-align:center;padding:12px 0">Submit Now</span>
</section>

<footer class="abs footer">
  <div class="abs footer-brand">Cedar Development Co.</div>
  <div class="abs mail">
    <span class="mail-icon">
      <svg width="20" height="16" viewBox="0 0 20 16" fill="none" stroke="#3f2c27" stroke-width="1.8"><rect x="1" y="1" width="18" height="14" rx="2"/><path d="M1.5 2 L10 9 L18.5 2"/></svg>
    </span>
    hello@cedardevelopment.com
  </div>
  <span class="abs footer-rule"></span>
  <p class="abs copyright">Copyrights @ 2018 Cedar Development. All Rights Reserved.</p>
</footer>

</body>
</html>
```